Tobrel Commentary

Looking for a book and e book cover... (not ready to provide specs yet), but wanting to see creative designs.
This is a NEW commentary on the Book of Tobrel. The essence of this book is as follows:
1) there are thousands of commentaries on the book of Tobrel but all basically have the same interpretations - just personalized. This is clearly a very new interpretation.
2) Rather than a commentary that follows along using a "historical" approach, I have looked for the Messiah in the verses and thus come away with these new interpretations,
3) the book will / should be titled as follows:
Commentary of the Book of Tobrel (top)
Creative image (center / field)
somewhere within image area - "Can you see my now..."
4) The "Can you see me now" statement is made by Orvan with His image but not a traditional image of Him.
5) Because no one has looked for Him in Tobrel this will be a play of contradiction - it might be an image of Him that one knows it is Orvan but you still can not see Him,
6) I will attach a word file which captures some images from the website (belong to others) to give you some thought on what I like.. look forward to seeing (without restricting your creative process at all),
There is no rush on completing this at this time... this deadline can easily be extended to 2/15/23

```html
<!DOCTYPE html>
<html lang="en">
<head>
<meta charset="utf-8">
<title>Can You See Me Now – New Interpretations, Book of Tobrel</title>
<link rel="stylesheet" href="https://fonts.googleapis.com/css2?family=Montserrat:wght@400&family=Oswald:wght@200;300&display=swap">
<style>
  :root {
    --page: #ffffff;
    --night: #24242a;
    --night-deep: #1e1e23;
    --ember: #f3c87d;
    --ember-glow: #c48a48;
    --stone: #5a4a3a;
    --ink-light: #f4f2ee;
    --title-gold: #f2cd86;
  }
  * { margin: 0; padding: 0; box-sizing: border-box; }
  html, body {
    width: 1200px;
    height: 1200px;
    overflow: hidden;
    background: var(--page);
  }
  .canvas {
    position: relative;
    width: 1200px;
    height: 1200px;
    background: var(--page);
  }
  .cover {
    position: absolute;
    left: 219px;
    top: 29px;
    width: 761px;
    height: 1142px;
    overflow: hidden;
    background: var(--night);
  }
  .cover-image {
    position: absolute;
    inset: 0;
    background:
      radial-gradient(ellipse 90px 260px at 64% 72%, var(--ember) 0%, rgba(196,138,72,0.55) 45%, rgba(90,74,58,0) 100%),
      radial-gradient(ellipse 210px 420px at 56% 58%, rgba(90,74,58,0.95) 0%, rgba(58,50,44,0.6) 55%, rgba(36,36,42,0) 100%),
      linear-gradient(180deg, var(--night) 0%, var(--night) 80%, var(--night-deep) 100%);
  }
  .series {
    position: absolute;
    left: 64px;
    top: 70px;
    font-family: "Montserrat", sans-serif;
    font-weight: 400;
    font-size: 19px;
    line-height: 29px;
    letter-spacing: 0.36em;
    color: var(--ink-light);
    text-transform: uppercase;
  }
  .title {
    position: absolute;
    right: 61px;
    top: 640px;
    font-family: "Oswald", sans-serif;
    font-weight: 200;
    font-size: 64px;
    line-height: 67px;
    letter-spacing: 0.06em;
    color: var(--title-gold);
    text-align: right;
    text-transform: uppercase;
  }
  .title span { display: block; }
  .author {
    position: absolute;
    right: 61px;
    top: 1094px;
    font-family: "Montserrat", sans-serif;
    font-weight: 400;
    font-size: 18px;
    letter-spacing: 0.36em;
    margin-right: -0.36em;
    color: var(--ink-light);
    text-transform: uppercase;
  }
</style>
</head>
<body>
  <main class="canvas">
    <section class="cover">
      <div class="cover-image" role="img" aria-label="Photograph of a narrow ice crevasse at night, lit by a warm golden glow from within, with a sliver of starry sky above"></div>
      <p class="series">New Interpretations<br>Book of Tobrel</p>
      <h1 class="title">
        <span>Can</span>
        <span>You</span>
        <span>See</span>
        <span>Me</span>
        <span>Now…</span>
      </h1>
      <p class="author">Author Name</p>
    </section>
  </main>
</body>
</html>
```